I am looking for business cards and letterhead

I want a high-level look for CEO's who want a concierge level leadership consultant and organization development strategist

This needs to go with my brand: simple, elegant, clean. Please improve on this design while using these fonts and colors

Here is my website: CorinneHalvers.com

```html
<!DOCTYPE html>
<html lang="en">
<head>
<meta charset="utf-8">
<title>Corinne Halvers – Business Card</title>
<link rel="stylesheet" href="https://fonts.googleapis.com/css2?family=Montserrat:wght@400;500;600;700&display=swap">
<style>
  :root {
    --page-bg: #ebe6df;
    --panel-dark-1: #17171a;
    --panel-dark-2: #3a3937;
    --panel-light: #e4ded5;
    --brand-blue: #1f5b97;
    --brand-gold: #d7a64e;
    --text-light: #d9d0c2;
    --card-shadow: rgba(40, 30, 20, 0.18);
  }
  * { margin: 0; padding: 0; box-sizing: border-box; }
  html, body {
    width: 1200px;
    height: 1047px;
    overflow: hidden;
    background: var(--page-bg);
    font-family: "Montserrat", Arial, sans-serif;
  }
  .business-card {
    position: absolute;
    left: 100px;
    top: 251px;
    width: 1000px;
    height: 545px;
    border-radius: 22px;
    overflow: hidden;
    box-shadow: 0 18px 40px var(--card-shadow);
  }
  .card-art {
    position: absolute;
    inset: 0;
    width: 1000px;
    height: 545px;
  }
  .holder-name {
    position: absolute;
    left: 40px;
    top: 58px;
    font-size: 37px;
    font-weight: 700;
    letter-spacing: 0.3px;
    color: var(--brand-blue);
  }
  .holder-title {
    position: absolute;
    left: 40px;
    top: 112px;
    font-size: 22px;
    font-weight: 400;
    letter-spacing: 0.6px;
    color: var(--text-light);
  }
  .address {
    position: absolute;
    left: 40px;
    top: 228px;
    font-size: 23px;
    line-height: 37px;
    letter-spacing: 0.6px;
    color: var(--text-light);
    font-style: normal;
  }
  .contact-list {
    position: absolute;
    left: 40px;
    top: 383px;
    list-style: none;
  }
  .contact-item {
    display: flex;
    align-items: center;
    height: 39px;
    font-size: 23px;
    letter-spacing: 0.6px;
    color: var(--text-light);
  }
  .contact-icon {
    width: 17px;
    height: 17px;
    margin-right: 14px;
    fill: var(--brand-blue);
  }
  .brand-mark {
    position: absolute;
    left: 526px;
    top: 73px;
    width: 400px;
    height: 400px;
    display: flex;
    align-items: center;
    justify-content: center;
    text-align: center;
    font-size: 34px;
    font-weight: 600;
    line-height: 44px;
    color: var(--brand-blue);
  }
</style>
</head>
<body>
  <article class="business-card">
    <svg class="card-art" viewBox="0 0 1000 545" aria-hidden="true">
      <defs>
        <linearGradient id="dark-panel" x1="0" y1="0" x2="1" y2="0.4">
          <stop offset="0" stop-color="var(--panel-dark-1)"/>
          <stop offset="0.55" stop-color="var(--panel-dark-2)"/>
          <stop offset="1" stop-color="var(--panel-dark-1)"/>
        </linearGradient>
      </defs>
      <rect class="dark-panel" width="1000" height="545" fill="url(#dark-panel)"/>
      <rect class="light-panel" x="740" width="260" height="545" fill="var(--panel-light)"/>
      <circle class="light-disc" cx="740" cy="275" r="290" fill="var(--panel-light)"/>
      <path class="blue-sweep" fill="var(--brand-blue)" fill-rule="evenodd"
        d="M450 275 A290 290 0 1 0 1030 275 A290 290 0 1 0 450 275 Z
           M464 275 A285 285 0 1 0 1034 275 A285 285 0 1 0 464 275 Z"/>
      <circle class="gold-ring" cx="726" cy="273" r="200" fill="none" stroke="var(--brand-gold)" stroke-width="4"/>
    </svg>

    <h1 class="holder-name">Corinne Halvers</h1>
    <p class="holder-title">Managing Director</p>

    <address class="address">Your address, City<br>State, Zip 1234</address>

    <ul class="contact-list">
      <li class="contact-item">
        <svg class="contact-icon" viewBox="0 0 16 16"><path d="M2 5c0-2 2-3 6-3s6 1 6 3v1.5h-3V5H5v1.5H2zM4 8h8l2 6H2z"/></svg>
        123 456 789
      </li>
      <li class="contact-item">
        <svg class="contact-icon" viewBox="0 0 16 16"><path d="M1 3h14v10H1zM2 4v1l6 4 6-4V4z"/></svg>
        info@CorinneHalvers.com
      </li>
      <li class="contact-item">
        <svg class="contact-icon" viewBox="0 0 16 16"><circle cx="8" cy="8" r="7"/></svg>
        CorinneHalvers.com
      </li>
    </ul>

    <div class="brand-mark">Corinne<br>Halvers</div>
  </article>
</body>
</html>
```